Business Card and Stationary for Maplecrest Baptist Day School
Maplecrest Baptist Day School
Business Card and Stationary for Maplecrest Baptist Day School - Childcare
Creative Brief
Bright & Fun-filled
Delia Fenwick
Day School Director
4817 W. Tollbridge Rd Hampton, VA 23671
dayschool@maplecrestbaptistexample.com
www.MCDaySchool-example.com
Walking in Faith, Growing Hearts, Nurturing Spirits (See uploaded logo) Theme Verse is: Luke 2:52 And Jesus increased in wisdom and stature, and in favour with God and man.
Hours of Operation: Monday - Friday 6am - 6pm See attached QR Code

```html
<!DOCTYPE html>
<html lang="en">
<head>
<meta charset="utf-8">
<title>Maplecrest Baptist Day School – Business Card</title>
<link href="https://fonts.googleapis.com/css2?family=Ubuntu:wght@400;500;700&display=swap" rel="stylesheet">
<style>
  :root {
    --page-bg: #eef0ec;
    --card-white: #ffffff;
    --band-grey: #5f6062;
    --icon-grey: #4a4b4d;
    --brand-green: #8cc63f;
    --brand-green-light: #a3d65a;
    --ink-dark: #3b3c3e;
    --ink-soft: #8a8b8d;
    --logo-blue: #2f7fc1;
  }
  * { box-sizing: border-box; margin: 0; padding: 0; }
  html, body {
    width: 1200px; height: 799px; overflow: hidden;
    background: var(--page-bg);
    font-family: "Ubuntu", sans-serif;
  }
  .business-card {
    position: absolute; left: 180px; top: 160px;
    width: 840px; height: 480px;
    background: var(--card-white);
    box-shadow: 0 12px 30px rgba(0,0,0,0.18);
    overflow: hidden;
  }
  .brand-block {
    position: absolute; left: 0; top: 70px; width: 460px;
    text-align: center;
  }
  .brand-tagline {
    font-size: 13px; color: var(--ink-soft); letter-spacing: 0.5px;
    margin-bottom: 14px;
  }
  .brand-mark {
    display: inline-flex; align-items: center; gap: 12px;
  }
  .brand-dot {
    width: 42px; height: 42px; border-radius: 50%;
    background: var(--brand-green);
  }
  .brand-name {
    font-weight: 700; font-size: 26px; color: var(--logo-blue);
    line-height: 1.15; text-align: left;
  }
  .address-band {
    position: absolute; left: 0; top: 300px; width: 460px; height: 56px;
    background: var(--band-grey);
    color: #fff; font-size: 15px;
    display: flex; align-items: center; justify-content: center;
    letter-spacing: 0.3px;
  }
  .contact-panel {
    position: absolute; left: 460px; top: 0; width: 380px; height: 480px;
    background: linear-gradient(100deg, var(--brand-green-light) 0%, var(--brand-green) 40%);
  }
  .person-name {
    position: absolute; left: 28px; top: 120px;
    font-size: 34px; font-weight: 700; color: #fff;
  }
  .person-title {
    position: absolute; left: 30px; top: 166px;
    font-size: 14px; font-weight: 500; letter-spacing: 5px; color: #fff;
  }
  .contact-list {
    position: absolute; right: 0; top: 236px; list-style: none;
  }
  .contact-item {
    display: flex; align-items: center; justify-content: flex-end;
    gap: 12px; height: 30px; margin-bottom: 10px;
    color: #fff; font-size: 15px;
  }
  .contact-item.is-small { font-size: 13px; }
  .contact-icon {
    width: 30px; height: 30px; background: var(--icon-grey);
    display: flex; align-items: center; justify-content: center;
  }
  .contact-icon svg { width: 16px; height: 16px; }
</style>
</head>
<body>
  <article class="business-card">
    <div class="brand-block">
      <p class="brand-tagline">Walking in Faith, Growing Hearts, Nurturing Spirits</p>
      <div class="brand-mark">
        <span class="brand-dot"></span>
        <span class="brand-name">Maplecrest Baptist<br>Day School</span>
      </div>
    </div>

    <div class="address-band">4817 W. Tollbridge Rd Hampton, VA 23671</div>

    <section class="contact-panel">
      <h1 class="person-name">Delia Fenwick</h1>
      <p class="person-title">DAY SCHOOL DIRECTOR</p>

      <ul class="contact-list">
        <li class="contact-item">757.555.0143
          <span class="contact-icon"><svg viewBox="0 0 16 16" fill="#fff"><path d="M3 1h3l1 4-2 1c1 2 3 4 5 5l1-2 4 1v3c0 1-1 2-2 2C7 15 1 9 1 3c0-1 1-2 2-2z"/></svg></span>
        </li>
        <li class="contact-item">757.555.0144
          <span class="contact-icon"><svg viewBox="0 0 16 16" fill="#fff"><rect x="4" y="1" width="8" height="4"/><rect x="1" y="6" width="14" height="6" rx="1"/><rect x="4" y="10" width="8" height="5" fill="#4a4b4d" stroke="#fff"/></svg></span>
        </li>
        <li class="contact-item is-small">dayschool@maplecrestbaptistexample.com
          <span class="contact-icon"><svg viewBox="0 0 16 16" fill="none" stroke="#fff" stroke-width="1.5"><rect x="1" y="3" width="14" height="10"/><path d="M1 3l7 6 7-6"/></svg></span>
        </li>
        <li class="contact-item">www.MCDaySchool-example.com
          <span class="contact-icon"><svg viewBox="0 0 16 16" fill="none" stroke="#fff" stroke-width="1.3"><circle cx="8" cy="8" r="6.5"/><ellipse cx="8" cy="8" rx="3" ry="6.5"/><path d="M1.5 8h13"/></svg></span>
        </li>
      </ul>
    </section>
  </article>
</body>
</html>
```